KESTREL BOILWORKS business card

We need a new business card for our company "Kestrel Boilworks". The company is very simple, we supply bulk heated water to the oilfield and industry. I have included a few images of cards that I like so that you have an idea of the direction I want to go. I will leave fonts up to the designer. I have also included our logo.
Updates

Hello Designers,  if there are any more submissions coming in you might consider using other background colors than black.  I am looking for a little bit of variety before making the decision.

Thanks,

Dean

Sorry, I meant to say background colors other than just black and white.

Thanks,

Dean

Target Market(s)

Ages 20 to 60. Oilfield consultants and Oil and Gas Companies

Industry/Entity Type

Business

Font styles to use
Sans Serif

Requirements
Must have
• Dean Varga

email info@kestrelboilworks-mail.com

Phone # 780-555-3817
Fax 780-555-2964

Site 317, Box 4, Comp 2, RR5
Corvin Flats, WR, T9K 4P3

11-07-52-3 W4M
Hwy 734 Between RR57 & RR58

**Must have our logo

Nice to have
• Would be nice to have " Bulk Heated Water" somewhere on the card

The logo with the flame large across the background might look ok? The name of the company is KESTREL BOILWORKS, but it probably isn't necessary to have the hot water under the logo all the time if you decide it looks better. As long as it is included somewhere on the card. The style of the Kestrel can change slightly (ie:; can be slanted).

The colors of the logo can change, but it might be nice to have the original color and logo somewhere small (corner?)

```html
<!DOCTYPE html>
<html lang="en">
<head>
<meta charset="utf-8">
<title>Kestrel Boilworks – Business Card</title>
<link rel="stylesheet" href="https://fonts.googleapis.com/css2?family=Arimo:wght@400;700&display=swap">
<style>
  :root {
    --backdrop: #9a9a98;
    --card-black: #0b0b0b;
    --card-white: #ffffff;
    --brand-sky: #5bb8dc;
    --brand-red: #e3262a;
    --band-blue: #1b86c0;
    --ink: #1a1a1a;
  }
  * { margin: 0; padding: 0; box-sizing: border-box; }
  html, body {
    width: 1200px; height: 1000px; overflow: hidden;
    background: var(--backdrop);
    font-family: "Arimo", Arial, sans-serif;
  }
  .card {
    position: absolute; left: 250px; width: 700px; height: 400px;
    overflow: hidden; box-shadow: 0 6px 18px rgba(0,0,0,.25);
  }
  .card-front { top: 60px; background: var(--card-black); }
  .card-back { top: 540px; background: var(--card-black); }

  .front-brand {
    position: absolute; inset: 0;
    display: flex; align-items: center; justify-content: center; gap: 22px;
  }
  .brand-dot { width: 70px; height: 70px; border-radius: 50%; background: var(--brand-sky); }
  .front-name {
    color: var(--brand-sky); font-weight: 700; font-size: 50px; line-height: 1.05;
    letter-spacing: 1px;
  }

  .back-shape { position: absolute; inset: 0; }
  .back-brand {
    position: absolute; left: 58px; top: 128px;
    display: flex; flex-direction: column; align-items: flex-start; gap: 12px;
  }
  .back-dot { width: 38px; height: 38px; border-radius: 50%; background: var(--band-blue); margin-left: 70px; }
  .back-name { color: var(--brand-red); font-weight: 700; font-size: 34px; line-height: 1.05; }

  .divider { position: absolute; left: 372px; top: 150px; width: 2px; height: 150px; background: var(--band-blue); }

  .contact { position: absolute; left: 392px; top: 146px; color: var(--ink); }
  .contact-name { font-size: 21px; margin-left: 30px; margin-bottom: 10px; }
  .contact-list { list-style: none; font-size: 13.5px; line-height: 19px; }
  .contact-list li { display: flex; align-items: flex-start; gap: 10px; }
  .contact-list svg { width: 16px; height: 16px; margin-top: 2px; flex: none; fill: var(--ink); }
  .address { display: block; }
</style>
</head>
<body>

<section class="card card-front" aria-label="Card front">
  <div class="front-brand">
    <span class="brand-dot"></span>
    <div class="front-name">KESTREL<br>BOILWORKS</div>
  </div>
</section>

<section class="card card-back" aria-label="Card back">
  <svg class="back-shape" viewBox="0 0 700 400" preserveAspectRatio="none">
    <path d="M0,400 L0,170 C110,70 280,40 700,40 L700,400 Z" fill="var(--card-white)"/>
    <rect x="0" y="325" width="700" height="22" fill="var(--band-blue)"/>
  </svg>

  <div class="back-brand">
    <span class="back-dot"></span>
    <div class="back-name">KESTREL<br>BOILWORKS</div>
  </div>

  <div class="divider"></div>

  <div class="contact">
    <div class="contact-name">Dean Varga</div>
    <ul class="contact-list">
      <li>
        <svg viewBox="0 0 16 16"><path d="M3 2h3l1.5 3.5-2 1.2a8 8 0 0 0 3.8 3.8l1.2-2L14 10v3a1 1 0 0 1-1 1A11 11 0 0 1 2 3a1 1 0 0 1 1-1z"/></svg>
        <span>Phone # 780 555 3817</span>
      </li>
      <li>
        <svg viewBox="0 0 16 16"><rect x="4" y="1" width="8" height="5"/><rect x="1" y="6" width="14" height="8" rx="1"/></svg>
        <span>Fax 780 555 2964</span>
      </li>
      <li>
        <svg viewBox="0 0 16 16"><path d="M1 3h14v10H1z M2 4l6 5 6-5" fill="none" stroke="currentColor" stroke-width="1.6"/></svg>
        <span>email info@kestrelboilworks-mail.com</span>
      </li>
      <li>
        <svg viewBox="0 0 16 16"><path d="M8 1a5 5 0 0 1 5 5c0 4-5 9-5 9S3 10 3 6a5 5 0 0 1 5-5zm0 3a2 2 0 1 0 0 4 2 2 0 0 0 0-4z"/></svg>
        <span class="address">Site 317 Box 4 , Comp 2, RR 5<br>Corvin Flats, WR, T9K 4P3<br>11-07-52-3W4M<br>Hwy 734 Between RR57 &amp; RR58</span>
      </li>
    </ul>
  </div>
</section>

</body>
</html>
```